strength and conditioning business focused on helping people move more efficiently

I need a business card designed for a Philadelphia based company called Trk Vlt Motion (pronounced Track Volt). We offer fitness professional services with the idea of helping people feel better and move optimally. We do this by designing and walking through individualized programs as well as minor soft tissue work. Our perfect client would be athletes but we will be marketing to parents who have children that are active They remember their former athletic days and want to get as close as possible back to that feeling. Attached will be the official logo and logo formats. I would love for the design to communicate trustworthy and creative. I would also love for the design to be square with rounded edges.

Target Market(s)

Parents of athletic children
former athletes
athletes

Industry/Entity Type

Fitness

Contact Information for Business Card

Business: Trk Vlt Performance
Name: Coach Garrett Ellison
Position: Strength and Conditioning Coach / Certified Personal Trainer
Contact: coach.ell@trkvlt-example.com
Text: (555)204-7719

Font styles to use
Serif
Sans Serif

Colors
fbee38
fbee3e
0255a3
3176b5
ffffff

Requirements
Must have
• use of logo
Nice to have
• Square design
rounded edges

```html
<!DOCTYPE html>
<html lang="en">
<head>
<meta charset="utf-8">
<title>Trk Vlt Motion — Business Card</title>
<link href="https://fonts.googleapis.com/css2?family=Open+Sans:wght@400;600;700;800&display=swap" rel="stylesheet">
<style>
  :root {
    --stage: #e6e6e6;
    --navy: #034a8c;
    --blue-text: #0b4f93;
    --yellow: #f5c40a;
    --card-light: #f4f4f4;
    --ink: #333333;
    --white: #ffffff;
  }
  * { margin: 0; padding: 0; box-sizing: border-box; }
  html, body { width: 1200px; height: 960px; overflow: hidden; }
  body {
    background: var(--stage);
    font-family: "Open Sans", Arial, sans-serif;
    position: relative;
  }
  .card {
    position: absolute;
    top: 274px;
    width: 403px;
    height: 403px;
    border-radius: 36px;
    overflow: hidden;
  }
  .card--front { left: 170px; background: var(--navy); }
  .card--back { left: 624px; background: var(--card-light); }

  .brand {
    position: absolute;
    left: 0; right: 0; top: 58px;
    text-align: center;
    color: var(--white);
    font-weight: 800;
  }
  .brand__dot {
    display: block;
    width: 58px; height: 58px;
    margin: 0 auto 22px;
    border-radius: 50%;
    background: var(--yellow);
  }
  .brand__name {
    font-size: 78px;
    line-height: 0.98;
    letter-spacing: 1px;
  }

  .contact-block { position: absolute; left: 37px; }
  .person { top: 114px; }
  .person__name {
    color: var(--blue-text);
    font-weight: 700;
    font-size: 17px;
    line-height: 24px;
  }
  .person__role {
    color: var(--ink);
    font-size: 13.5px;
    line-height: 19.5px;
  }
  .company { top: 266px; }
  .company__name {
    color: var(--blue-text);
    font-weight: 700;
    font-size: 15px;
    line-height: 22px;
    margin-bottom: 7px;
  }
  .contact-list { list-style: none; }
  .contact-list li {
    display: flex;
    align-items: center;
    gap: 3px;
    color: var(--ink);
    font-size: 13.5px;
    line-height: 19px;
  }
  .contact-list svg { width: 14px; height: 14px; flex: none; }
</style>
</head>
<body>
  <section class="card card--front" aria-label="Card front">
    <div class="brand">
      <span class="brand__dot" aria-hidden="true"></span>
      <div class="brand__name">Trk Vlt<br>Motion</div>
    </div>
  </section>

  <section class="card card--back" aria-label="Card back">
    <div class="contact-block person">
      <div class="person__name">Coach Garrett Ellison</div>
      <div class="person__role">Strength and Conditioning Coach</div>
      <div class="person__role">Certified Personal Trainer</div>
    </div>
    <div class="contact-block company">
      <div class="company__name">Trk Vlt Performance</div>
      <ul class="contact-list">
        <li>
          <svg viewBox="0 0 14 14" aria-hidden="true"><circle cx="7" cy="7" r="7" fill="#0b4f93"/><path d="M4.3 3.6l1.4-.4.8 1.8-.9.7c.4.9 1.1 1.6 2 2l.7-.9 1.8.8-.4 1.4c-3 .2-5.6-2.4-5.4-5.4z" fill="#f5c40a"/></svg>
          (555) 204-7719
        </li>
        <li>
          <svg viewBox="0 0 14 14" aria-hidden="true"><circle cx="7" cy="7" r="7" fill="#0b4f93"/><rect x="3.3" y="4.5" width="7.4" height="5" fill="#f5c40a"/><path d="M3.3 4.5L7 7.5l3.7-3" fill="none" stroke="#0b4f93" stroke-width="0.8"/></svg>
          coach.ell@trkvlt-example.com
        </li>
        <li>
          <svg viewBox="0 0 14 14" aria-hidden="true"><circle cx="7" cy="7" r="7" fill="#0b4f93"/><circle cx="7" cy="7" r="3.8" fill="none" stroke="#f5c40a" stroke-width="0.9"/><path d="M3.2 7h7.6M7 3.2c-1.6 2.4-1.6 5.2 0 7.6M7 3.2c1.6 2.4 1.6 5.2 0 7.6" fill="none" stroke="#f5c40a" stroke-width="0.8"/></svg>
          www.trkvlt-example.com
        </li>
      </ul>
    </div>
  </section>
</body>
</html>
```